Zielgruppe
für meinen ambulanten Pflegedienst hätte ich gerne Visitenkarten. #
Für zwei Personen mir jeweils gleicher Geschäftsadresse.
KaLuVo Die flinke Pflegehilfe GmbH
www.Kaluvo.de
Das Logo bitte der Homepage entnehmen.
Entwurf bitte für eine Visitenkarte und Briefpapier
Des weiteren wird ein Design für einen runden Leuchtkasten Durchmesser 90 cm benötigt.
Auf dem Briefpapier ist dass noch Kontonummer und Steuernummer zu ergänzen
Aufgabenstellung
Die Visitenkarte sollte elegant und luxuriös sein.

```html
<!DOCTYPE html>
<html lang="de">
<head>
<meta charset="utf-8">
<title>KaLuVo – Leuchtkasten</title>
<link href="https://fonts.googleapis.com/css2?family=Open+Sans:wght@300;600&display=swap" rel="stylesheet">
<style>
  :root {
    --page-bg: #eeeeec;
    --ring-green: #5a9a3a;
    --inner-green: #b3d6a4;
    --photo-warm: #d9c8b4;
    --photo-cool: #b9c8b0;
    --ring-text: #f4f8ef;
    --ink-dark: #2a2a28;
    --accent-red: #c0172e;
  }
  html, body {
    margin: 0;
    width: 1200px;
    height: 900px;
    overflow: hidden;
    background: var(--page-bg);
  }
  .lightbox-face {
    display: block;
    width: 1200px;
    height: 900px;
  }
  .ring-text {
    font-family: "Open Sans", sans-serif;
    font-weight: 600;
    fill: var(--ring-text);
    letter-spacing: 2px;
  }
  .ring-text--claim { font-size: 40px; }
  .ring-text--phone { font-size: 52px; letter-spacing: 1px; }
  .brand-name {
    font-family: "Open Sans", sans-serif;
    font-weight: 300;
    font-size: 84px;
    fill: var(--ink-dark);
    letter-spacing: 1px;
  }
  .brand-tagline {
    font-family: "Open Sans", sans-serif;
    font-weight: 600;
    font-size: 26px;
    fill: var(--ink-dark);
  }
</style>
</head>
<body>
<svg class="lightbox-face" viewBox="0 0 1200 900" xmlns="http://www.w3.org/2000/svg">
  <defs>
    <clipPath id="inner-disc">
      <circle cx="600" cy="450" r="330"/>
    </clipPath>
    <linearGradient id="photo-tone" x1="0" y1="0" x2="1" y2="1">
      <stop offset="0" stop-color="var(--photo-cool)"/>
      <stop offset="0.5" stop-color="var(--photo-warm)"/>
      <stop offset="1" stop-color="var(--photo-cool)"/>
    </linearGradient>
    <path id="claim-arc" d="M 248 578 A 375 375 0 1 1 952 578"/>
    <path id="phone-arc" d="M 262 645 A 390 390 0 0 0 938 645"/>
  </defs>

  <circle class="outer-ring" cx="600" cy="450" r="420" fill="var(--ring-green)"/>
  <circle class="inner-disc" cx="600" cy="450" r="330" fill="var(--inner-green)"/>

  <g class="hero-photo" clip-path="url(#inner-disc)" role="img" aria-label="Foto eines lächelnden älteren Paares">
    <path d="M 260 110 L 940 110 L 940 300 L 260 365 Z" fill="url(#photo-tone)"/>
  </g>

  <text class="ring-text ring-text--claim">
    <textPath href="#claim-arc" startOffset="50%" text-anchor="middle">SERVICE - KRANKENPFLEGE AMBULANTER</textPath>
  </text>

  <g class="brand-lockup">
    <circle cx="420" cy="470" r="42" fill="var(--accent-red)"/>
    <text class="brand-name" x="500" y="500">KALUVO</text>
    <text class="brand-tagline" x="504" y="545">Die flinke Pflegehilfe</text>
  </g>

  <g class="phone-icon" transform="translate(600 640)">
    <circle r="42" fill="none" stroke="var(--accent-red)" stroke-width="3"/>
    <path d="M -14 -22 C -24 -8, -16 16, 8 26 L 16 18 L 6 8 L 0 12 C -8 6, -10 -2, -8 -10 L -2 -14 L -6 -28 Z" fill="var(--accent-red)"/>
  </g>

  <text class="ring-text ring-text--phone">
    <textPath href="#phone-arc" startOffset="50%" text-anchor="middle">+49 030 555-01234</textPath>
  </text>
</svg>
</body>
</html>
```